Menu design for a modern Pizza restaurant

We need a menu design which is visually attractive but also user friendly.
We want it to be A3 but fold in just like the Tonk'd menu attached.
We also want colourful and fun like our branding is.
I have attached another menu example from Ul Pizza which is laid out very well but needs colour.
Also attached is Merno menu which we like the design of, just needs colour.
Attached is our imagery and logo.
And lastly is our menu attached.
We really need it in 24 hours if possible.

Target Market(s)

All Pizza eaters in our area

Industry/Entity Type

Hospitality

Requirements
Must have
• Bold, colourful and fun

```html
<!DOCTYPE html>
<html lang="en">
<head>
<meta charset="utf-8">
<title>Pizza Menu</title>
<link rel="stylesheet" href="https://fonts.googleapis.com/css2?family=Montserrat:wght@600;700;800&family=Nunito+Sans:wght@300;400;600&display=swap">
<style>
  :root {
    --backdrop: #5fd3f3;
    --paper: #f4f4f1;
    --pattern-light: #bfe6ec;
    --pattern-deep: #8fd0da;
    --teal: #13808f;
    --frame-blue: #1a8fc4;
    --accent-warm: #f2a93b;
    --ink: #232323;
    --ink-soft: #454545;
  }
  * { margin: 0; padding: 0; box-sizing: border-box; }
  html, body { width: 1200px; height: 761px; overflow: hidden; }
  body {
    background: var(--backdrop);
    font-family: "Nunito Sans", Arial, sans-serif;
    color: var(--ink);
    position: relative;
  }
  .menu-sheet {
    position: absolute;
    left: 60px; top: 36px;
    width: 1080px; height: 690px;
    background: var(--paper);
    box-shadow: 0 8px 28px rgba(0,60,90,.22);
  }
  .border-pattern {
    position: absolute; inset: 0;
    background: linear-gradient(135deg, var(--pattern-light), var(--pattern-deep));
  }
  .menu-inner {
    position: absolute; inset: 44px;
    background: var(--paper);
    display: grid;
    grid-template-columns: 1fr 1fr;
  }
  .pizza-list {
    padding: 22px 40px 20px 34px;
    border-right: 2px dashed var(--pattern-deep);
  }
  .pizza { margin-bottom: 11px; }
  .pizza-name {
    font-family: "Montserrat", Arial, sans-serif;
    font-weight: 800;
    font-size: 15px;
    line-height: 1.2;
    color: var(--teal);
  }
  .pizza-name::before {
    content: "";
    display: inline-block;
    width: 8px; height: 8px;
    border-radius: 50%;
    background: var(--accent-warm);
    margin-right: 7px;
    vertical-align: 2px;
  }
  .pizza-desc {
    font-size: 12px;
    line-height: 1.3;
    color: var(--ink-soft);
    padding-left: 15px;
  }
  .build-panel { padding: 22px 30px 22px 34px; }
  .build-box {
    height: 100%;
    border: 4px solid var(--frame-blue);
    padding: 22px 24px;
    display: grid;
    grid-template-columns: 1fr 1.15fr 1fr;
    column-gap: 16px;
  }
  .group { margin-bottom: 22px; }
  .group-title {
    font-family: "Montserrat", Arial, sans-serif;
    font-weight: 800;
    font-size: 13px;
    color: var(--frame-blue);
    margin-bottom: 4px;
    padding-bottom: 2px;
    border-bottom: 2px solid var(--accent-warm);
    display: inline-block;
  }
  .group ul { list-style: none; }
  .group li {
    font-size: 13px;
    line-height: 1.38;
    color: var(--ink-soft);
  }
</style>
</head>
<body>
  <div class="menu-sheet">
    <div class="border-pattern" role="img" aria-label="Repeating border of small eyes, hearts and pizza slices in teal"></div>
    <div class="menu-inner">
      <section class="pizza-list">
        <div class="pizza"><p class="pizza-name">Mushroom &amp; truffle</p><p class="pizza-desc">Mushroom &amp; thyme, truffle oil, mozzarella, gorgonzola, fior di latte</p></div>
        <div class="pizza"><p class="pizza-name">Formaggio amore</p><p class="pizza-desc">Buffalo mozzarella, gorgonzola, fior di latte</p></div>
        <div class="pizza"><p class="pizza-name">Garlic pizza</p><p class="pizza-desc">confit garlic, buffalo mozzarella, fresh garlic, rosemary, extra virgin olive oil, sea salt black pepper,</p></div>
        <div class="pizza"><p class="pizza-name">Sage and pumpkin</p><p class="pizza-desc">Extra virgin olive oil, pumpkin, gorgonzola, scarmoza bianca, pine nuts, fior de latte, sage</p></div>
        <div class="pizza"><p class="pizza-name">Prosciutto</p><p class="pizza-desc">tomato base, fresh tomato, fresh basil, fior di latte, prosciutto, rocket, garlic oil, buffalo mozzarella</p></div>
        <div class="pizza"><p class="pizza-name">Carnivore</p><p class="pizza-desc">Bbq, beef, bacon, chicken, sopressa, onion, capsicum, tomato, mozzarella</p></div>
        <div class="pizza"><p class="pizza-name">Lamb</p><p class="pizza-desc">tomato base, roasted capsicum, eggplant, sun dried tomatoes, lamb, red onion, garlic yogurt, and rocket</p></div>
        <div class="pizza"><p class="pizza-name">Veg your heart out</p><p class="pizza-desc">Tomato base, roasted capsicum, broccoli, eggplant, zucchini, mushrooms, onion confit, kale, mozzarella, fior di latte, garlic oil</p></div>
        <div class="pizza"><p class="pizza-name">Falafel</p><p class="pizza-desc">Falafel, tomato, red onion, zucchini, capsicum, olives, goat cheese, garlic yogurt</p></div>
        <div class="pizza"><p class="pizza-name">Pepperoni</p><p class="pizza-desc">Calabrese salami, cherry tomato, goats cheese, mozzarella</p></div>
      </section>
      <section class="build-panel">
        <div class="build-box">
          <div class="build-col">
            <div class="group"><p class="group-title">Super</p><ul><li>wholemeal base</li></ul></div>
            <div class="group"><p class="group-title">Base</p><ul><li>Tomato</li><li>Pesto</li><li>Hoisin</li><li>BBQ</li><li>Olive oil</li></ul></div>
            <div class="group"><p class="group-title">Protein</p><ul><li>Beef</li><li>Chicken</li><li>Duck</li><li>Lamb</li><li>Bacon</li><li>Sopressa</li><li>Calabrese salami</li><li>Prosciutto</li><li>Ham</li><li>Anchovies</li></ul></div>
          </div>
          <div class="build-col">
            <div class="group"><p class="group-title">Fresh</p><ul><li>Broccoli</li><li>Kale</li><li>Capsicum</li><li>Tomato</li><li>Cherry tomatoes</li><li>Olives</li><li>Pineapple</li><li>Red onion</li><li>Caramelised onion</li><li>Artichoke</li><li>Zucchini</li><li>Carrot</li><li>Coriander</li><li>Nectarine</li><li>Mushroom</li><li>Chilli flakes</li><li>Fresh chilli</li><li>Sun dried tomato</li><li>Egg plant</li><li>Basil</li><li>Baby spinach</li></ul></div>
          </div>
          <div class="build-col">
            <div class="group"><p class="group-title">Extras</p><ul><li>Feta</li><li>Goats cheese</li><li>Eggs</li></ul></div>
            <div class="group"><p class="group-title">Sauces:</p><ul><li>Tomato</li><li>BBQ</li><li>Mayonnaise</li><li>Aioli</li><li>Dill aioli</li><li>Garlic</li><li>Blue cheese</li><li>Hot sauce</li><li>Mustard</li><li>Siracha Chilli</li></ul></div>
          </div>
        </div>
      </section>
    </div>
  </div>
</body>
</html>
```